Criação de Kit Layout de Posts para Redes Sociais (Facebook, Instagram e etc) para Esportes
" Ofereço serviços de personal trainer para alunos em academias, condomínios, parques, etc.; serviços de personal trainer on-line ao vivo; e serviços de consultoria para prescrição de treinos (sem o acompanhamento durante a execução em si dos treinos) "

```html
<!DOCTYPE html>
<html lang="pt-BR">
<head>
<meta charset="UTF-8">
<title>Rafael Moreira Personal Trainer – Post</title>
<link rel="stylesheet" href="https://fonts.googleapis.com/css2?family=Montserrat:ital,wght@0,700;0,800;0,900;1,700;1,800;1,900&display=swap">
<style>
  :root {
    --green: #2bdc3c;
    --green-dark: #149a22;
    --ink: #141414;
    --panel: #1b1d1b;
    --white: #ffffff;
    --skin: #b58a6e;
    --wall: #5a5752;
  }
  * { margin: 0; padding: 0; box-sizing: border-box; }
  html, body { width: 1200px; height: 1200px; overflow: hidden; background: var(--ink); }
  .post {
    position: relative;
    width: 1200px; height: 1200px;
    overflow: hidden;
    font-family: "Montserrat", Arial, sans-serif;
    background: radial-gradient(ellipse at 30% 40%, #3a3a38 0%, #1e1e1d 55%, #111 100%);
    color: var(--white);
  }
  .photo {
    position: absolute;
    left: 380px; top: 0;
    width: 820px; height: 1200px;
    background:
      radial-gradient(ellipse 260px 420px at 58% 42%, var(--skin) 0%, rgba(181,138,110,0.55) 45%, rgba(90,87,82,0) 75%),
      linear-gradient(90deg, rgba(30,30,29,1) 0%, rgba(70,68,64,0.9) 30%, var(--wall) 60%, #3b3935 100%);
  }
  .decor { position: absolute; inset: 0; width: 1200px; height: 1200px; }
  .brand {
    position: absolute;
    left: 20px; top: 20px;
    width: 556px; height: 232px;
    background: var(--panel);
    border: 4px solid var(--green);
    display: flex; flex-direction: column; align-items: center; justify-content: center;
    gap: 10px;
  }
  .brand__mark { width: 46px; height: 46px; background: var(--green); }
  .brand__name { font-weight: 800; font-size: 50px; letter-spacing: 1px; color: var(--white); }
  .brand__role {
    font-weight: 800; font-size: 24px; letter-spacing: 3px;
    color: var(--green); text-transform: uppercase;
    border-top: 3px solid var(--green); padding-top: 6px;
  }
  .headline {
    position: absolute; left: 52px; top: 372px;
    font-weight: 900; font-style: italic;
    font-size: 88px; line-height: 1.02;
    text-transform: uppercase;
    text-shadow: 6px 6px 0 #000;
  }
  .doubt {
    position: absolute; left: 52px; top: 752px;
    font-weight: 900; font-style: italic; font-size: 54px;
    text-transform: uppercase; text-shadow: 4px 4px 0 #000;
  }
  .tagline {
    position: absolute; left: 52px; top: 828px;
    font-weight: 800; font-style: italic; font-size: 37px; line-height: 1.2;
    color: var(--green); text-shadow: 3px 3px 0 #000;
  }
  .cta {
    position: absolute; left: 20px; top: 972px;
    width: 544px; height: 74px;
    background: var(--panel);
    border: 4px solid var(--green);
    display: flex; align-items: center; padding-left: 44px;
    font-weight: 900; font-style: italic; font-size: 32px; text-transform: uppercase;
  }
  .contacts {
    position: absolute; left: 20px; top: 1064px;
    width: 560px; height: 118px;
    background: rgba(20,20,20,0.92);
    list-style: none;
    padding: 8px 0 0 22px;
  }
  .contacts__item {
    display: flex; align-items: center; gap: 14px;
    font-weight: 700; font-size: 26px; height: 36px;
  }
  .contacts__icon { width: 26px; height: 26px; flex: none; }
</style>
</head>
<body>
<main class="post">
  <div class="photo" role="img" aria-label="Foto de uma mulher em roupa de treino mostrando o abdômen, em frente a uma parede de concreto escura"></div>

  <svg class="decor" viewBox="0 0 1200 1200" aria-hidden="true">
    <!-- top stripe bar -->
    <g fill="var(--green)">
      <polygon points="610,22 690,22 675,42 595,42"/>
      <polygon points="720,22 800,22 785,42 705,42"/>
      <polygon points="830,22 910,22 895,42 815,42"/>
      <polygon points="940,22 1020,22 1005,42 925,42"/>
      <polygon points="1050,22 1130,22 1115,42 1035,42"/>
    </g>
    <!-- diagonal bands -->
    <polygon points="0,700 420,1200 300,1200 0,850" fill="var(--green-dark)" opacity="0.85"/>
    <polygon points="580,1200 900,740 960,740 650,1200" fill="var(--green)"/>
    <polygon points="700,1200 1000,760 1040,760 750,1200" fill="var(--green-dark)"/>
    <polygon points="0,560 240,560 0,860" fill="#0f0f0f" opacity="0.6"/>
    <polygon points="1000,1200 1200,930 1200,1000 1060,1200" fill="var(--green)"/>
    <!-- frame -->
    <rect x="6" y="6" width="1188" height="1188" fill="none" stroke="#0b0b0b" stroke-width="12"/>
    <g fill="var(--green)">
      <rect x="660" y="1176" width="70" height="14"/>
      <rect x="760" y="1176" width="70" height="14"/>
      <rect x="860" y="1176" width="70" height="14"/>
      <rect x="960" y="1176" width="70" height="14"/>
      <rect x="1060" y="1176" width="70" height="14"/>
    </g>
  </svg>

  <header class="brand">
    <span class="brand__mark"></span>
    <span class="brand__name">RAFAEL MOREIRA</span>
    <span class="brand__role">Personal Trainer</span>
  </header>

  <h1 class="headline">Quando a<br>gente quer<br>a gente faz</h1>
  <p class="doubt">Não tenha dúvida!</p>
  <p class="tagline">Com um personal<br>você nunca estara sozinho</p>

  <div class="cta">Entre em contato</div>

  <ul class="contacts">
    <li class="contacts__item">
      <svg class="contacts__icon" viewBox="0 0 24 24"><circle cx="12" cy="12" r="10.5" fill="none" stroke="#fff" stroke-width="2"/><path d="M8.5 7.5c.5-.5 1.2-.4 1.5.2l.8 1.6c.2.4.1.9-.2 1.2l-.6.6c.6 1.3 1.6 2.3 2.9 2.9l.6-.6c.3-.3.8-.4 1.2-.2l1.6.8c.6.3.7 1 .2 1.5l-.8.8c-.7.7-1.8.8-2.7.3-2.2-1.2-4-3-5.2-5.2-.5-.9-.4-2 .3-2.7z" fill="#fff"/></svg>
      <span>11 98765-4321</span>
    </li>
    <li class="contacts__item">
      <svg class="contacts__icon" viewBox="0 0 24 24"><circle cx="12" cy="12" r="10" fill="#fff"/></svg>
      <span>@personal_rafaelmoreira</span>
    </li>
    <li class="contacts__item">
      <svg class="contacts__icon" viewBox="0 0 24 24"><rect x="2" y="5" width="20" height="14" rx="2" fill="#fff"/><path d="M3 6l9 7 9-7" fill="none" stroke="#141414" stroke-width="2"/></svg>
      <span>personal.rafael@mailbox.com</span>
    </li>
  </ul>
</main>
</body>
</html>
```